Clockharbour Homepage Banner 1060 W x 100 H

Please see the attached 'word' document (Also copied below)
Feel free to use any images or logos from our website.
www.clockharbour.com.au

Background:
We are an Australian based official watch distributor/online retailer of international watch brands.

We require a new banner ad (1060 W x 100 H) to replace the existing one on our homepage www.clockharbour.com.au & wish to convey the following information:
*(Please feel free to alter wording, include or exclude points below & generally take creative license (with commercial reality in mind). We sell some luxury watches, so it must look professional & maintain a luxury look & feel.)

Clockharbour Direct:
Revolutionising the retail watch market !

- Buy direct from the official distributor & get world competitive
online prices (with full international warranty, & all original
papers, box & invoice)

- Eliminate all risk of fakes & non-existent factory warranty from
'grey' market sellers

- Free worldwide delivery over A$300

- Order online & 'try-on' in the comfort of your own home.
If you're not 100% happy, just post it back for a full refund or
exchange within 30 days

- Prefer to see & try on before purchase? Visit one of our retail
partner stores.

*** Feel free to copy any images from our website
www.clockharbour.com.au
Updates

Target Market(s)

Luxury watches

Industry/Entity Type

Retail

Font styles to use
Sans Serif

Requirements
Must have
• Visual imagery, text
Nice to have
• Feel free to use your creativity...
Should not have
• Cheap looking or tacky images. We sell some luxury watches, so we need to keep a professional & luxury image.

```html
<!DOCTYPE html>
<html lang="en">
<head>
<meta charset="utf-8">
<title>Clockharbour Direct – Free worldwide delivery banner</title>
<link rel="stylesheet" href="https://fonts.googleapis.com/css2?family=Questrial&display=swap">
<style>
  :root {
    --bg: #ffffff;
    --ink-navy: #1a2a6b;
    --sky-pale: #e3f1fb;
    --sky-light: #9fd0f2;
    --sky-mid: #4aa3e6;
    --sky-deep: #1673d1;
    --watch-dark: #1d1f22;
    --watch-steel: #4a4d52;
    --watch-orange: #d8672a;
  }
  html, body {
    margin: 0;
    padding: 0;
    width: 1200px;
    height: 113px;
    overflow: hidden;
    background: var(--bg);
  }
  .banner {
    position: relative;
    width: 1200px;
    height: 113px;
    overflow: hidden;
    background: var(--bg);
  }
  .banner__product {
    position: absolute;
    left: 0;
    top: 0;
    width: 126px;
    height: 113px;
    background:
      radial-gradient(circle at 62% 50%, var(--watch-orange) 0 18%, transparent 40%),
      radial-gradient(circle at 58% 50%, var(--watch-steel) 0 48%, var(--watch-dark) 62%, transparent 64%),
      var(--bg);
  }
  .banner__headline {
    position: absolute;
    left: 345px;
    top: 33px;
    margin: 0;
    font-family: "Questrial", "Century Gothic", sans-serif;
    font-weight: 400;
    font-size: 33px;
    line-height: 1.2;
    letter-spacing: 0.2px;
    color: var(--ink-navy);
    white-space: nowrap;
  }
  .banner__swoosh {
    position: absolute;
    right: 0;
    top: 0;
    width: 1200px;
    height: 113px;
  }
</style>
</head>
<body>
  <div class="banner">
    <div class="banner__product" role="img" aria-label="Black chronograph wristwatch with orange racing-stripe dial"></div>

    <svg class="banner__swoosh" viewBox="0 0 1200 113" aria-hidden="true">
      <defs>
        <linearGradient id="swoosh-fill" x1="0" y1="0" x2="1" y2="0">
          <stop offset="0" stop-color="var(--sky-light)"/>
          <stop offset="1" stop-color="var(--sky-mid)"/>
        </linearGradient>
        <linearGradient id="arrow-fill" x1="0" y1="1" x2="0" y2="0">
          <stop offset="0" stop-color="var(--sky-deep)"/>
          <stop offset="1" stop-color="var(--sky-mid)"/>
        </linearGradient>
      </defs>
      <path class="swoosh__pale" d="M1045 0 C1095 28 1100 82 1082 113 L1200 113 L1200 0 Z" fill="var(--sky-pale)"/>
      <path class="swoosh__light" d="M1068 0 C1118 32 1120 84 1100 113 L1200 113 L1200 0 Z" fill="url(#swoosh-fill)"/>
      <path class="swoosh__deep" d="M1110 0 C1150 36 1148 88 1128 113 L1200 113 L1200 0 Z" fill="var(--sky-deep)" opacity="0.85"/>

      <g class="arrow-icon">
        <path d="M1030 106 C1060 90 1066 56 1040 30" fill="none" stroke="url(#arrow-fill)" stroke-width="13" stroke-linecap="round"/>
        <path d="M1020 12 L1054 22 L1032 44 Z" fill="var(--sky-mid)"/>
      </g>
    </svg>

    <p class="banner__headline">Free worldwide delivery over A$300</p>
  </div>
</body>
</html>
```